IT COMPANYcutting edge tec business card

we are IT company that building any apps.
we need business card in japanese and english
You don’t have to include all information in front one you can attach part of that information to back-side
company name : 株式会社ひかりの丘 (BRIGHTHILL Inc.)
concept : cutting-edge technology
role : 取締役 (director)
name : 呉 炫秀 (Oh Hyeonsuk)
post number : 154-0038
address : 東京都世田谷区西若葉台5-14-8 (5-14-8, Nishiwakabadai, Setagaya Ku, Tokyo To, 154-0038, Japan)
Tel:+81-3-5917-2846
Mobile:+81-80-7253-3169
Email : hoh@brighthill-lab.com
website : www.brighthill-lab.com

we dont have logo so please make it as well
we also looking for designer who can make homapage design.

Contact Information for Business Card

cutting-edge design and modern for IT

Font styles to use
Sans Serif

Colors
34a6d7
33b8a4
6092c4
3377b5
886aae
6b449b
b868aa
a64599

Requirements
Must have
• Simple but designed

```html
<!DOCTYPE html>
<html lang="ja">
<head>
<meta charset="utf-8">
<title>BRIGHTHILL Inc. Business Card</title>
<link rel="stylesheet" href="https://fonts.googleapis.com/css2?family=Noto+Sans+JP:wght@400;500&display=swap">
<style>
  :root {
    --bg: #d9d9db;
    --card: #ffffff;
    --brand-blue: #34a6d7;
    --brand-mid: #3377b5;
    --brand-purple: #6b449b;
    --text-purple: #5e3f8f;
    --wave-light: #e4f3fa;
    --wave-mid: #cfe9f4;
    --shadow: rgba(0, 0, 0, 0.18);
  }
  * { box-sizing: border-box; margin: 0; padding: 0; }
  html, body {
    width: 1200px;
    height: 900px;
    overflow: hidden;
    background: radial-gradient(ellipse at 50% 40%, #ececed 0%, var(--bg) 75%);
    font-family: "Noto Sans JP", sans-serif;
  }
  .stage { position: relative; width: 1200px; height: 900px; }

  .card {
    position: absolute;
    width: 560px;
    height: 340px;
    background: var(--card);
    box-shadow: 0 10px 30px var(--shadow);
    overflow: hidden;
  }
  .card--front { left: 60px; top: 100px; }
  .card--back  { left: 580px; top: 470px; }

  .wave-area {
    position: absolute;
    right: 0;
    top: 0;
    width: 380px;
    height: 340px;
    background: linear-gradient(160deg, var(--wave-light) 0%, var(--wave-mid) 45%, rgba(255,255,255,0) 80%);
  }

  .brand {
    position: absolute;
    display: flex;
    align-items: center;
    gap: 10px;
    color: var(--brand-mid);
    font-weight: 500;
  }
  .brand__dot {
    flex: none;
    border-radius: 50%;
    background: var(--brand-mid);
  }
  .brand__names { display: flex; flex-direction: column; line-height: 1.25; }

  .card--front .brand { left: 34px; top: 128px; font-size: 15px; }
  .card--front .brand__dot { width: 30px; height: 30px; }
  .card--front .brand__jp { font-size: 12px; }

  .details {
    position: absolute;
    left: 230px;
    top: 36px;
    color: var(--text-purple);
    font-size: 15px;
    line-height: 1.45;
  }
  .details__role, .details__name { font-size: 16px; }

  .contact {
    position: absolute;
    left: 230px;
    top: 250px;
    font-size: 16px;
    line-height: 1.55;
  }
  .contact__email { color: var(--text-purple); }
  .contact__web { color: var(--brand-blue); }

  .card--back .brand {
    left: 50%;
    top: 50%;
    transform: translate(-50%, -50%);
    font-size: 30px;
    gap: 16px;
  }
  .card--back .brand__dot { width: 64px; height: 64px; }
  .card--back .brand__jp { font-size: 20px; }
</style>
</head>
<body>
<main class="stage">

  <section class="card card--front">
    <div class="wave-area" role="img" aria-label="Flowing fine wave line pattern in light blue"></div>

    <div class="brand">
      <span class="brand__dot"></span>
      <div class="brand__names">
        <span class="brand__en">BRIGHTHILL Inc.</span>
        <span class="brand__jp">株式会社ひかりの丘</span>
      </div>
    </div>

    <div class="details">
      <p class="details__role">取締役</p>
      <p class="details__name">呉 炫秀</p>
      <p>Post number:154-0038</p>
      <p>東京都世田谷区西若葉台5-14-8</p>
      <p>Tel:+81-3-5917-2846</p>
      <p>Mobile:+81-80-7253-3169</p>
    </div>

    <div class="contact">
      <p class="contact__email">Email : hoh@brighthill-lab.com</p>
      <p class="contact__web">www.brighthill-lab.com</p>
    </div>
  </section>

  <section class="card card--back">
    <div class="brand">
      <span class="brand__dot"></span>
      <div class="brand__names">
        <span class="brand__en">BRIGHTHILL Inc.</span>
        <span class="brand__jp">株式会社ひかりの丘</span>
      </div>
    </div>
  </section>

</main>
</body>
</html>
```